Website for Torvik Capital

We need a new web design for a company based in Chicago called "Torvik Capital". TVK provides portfolio management and financial advice using primarily income oriented strategies, such as, dividend paying stocks and preferred stocks. Our niche is utilizing conservative option strategies to help generate income and minimize risk. We are looking for a clean-cut and streamline professional site that is both appealing and user friendly. We would like the main colors to be the dark blue and bright green of our logo. Depending on cost and ease, we may want a designer to give us the completed website, including the coding, etc.

Target Market(s)

20-80 year old affluent investors seeking portfolio management and investment advice.

Industry/Entity Type

Conservative

Requirements
Must have
• -our logo
-main tabs: home, about us, our philosophy, our services, investment strategy, compliance, contact us
-our phone number visible and conveniently placed on each page
Nice to have
• -conveniently placed login button for current clients
-conveniently placed "quick contact" box on home page with spaces for first name, last name, email, phone number, and a blank box for their question or comment
-check us out on Facebook and Twitter logos/buttons
-we like the idea of rotating pictures on top of page, but we aren't sure whether or not we definitely want that
Should not have
• -no trees
-no clocks
-no timers
-no crowns
-no plants

```html
<!DOCTYPE html>
<html lang="en">
<head>
<meta charset="utf-8">
<title>Torvik Capital</title>
<link rel="stylesheet" href="https://fonts.googleapis.com/css2?family=Open+Sans:wght@400;600;700&family=Noto+Serif:ital,wght@0,700;1,700&display=swap">
<style>
:root{
  --navy:#0b1a9c;
  --navy-deep:#000e7a;
  --green:#86c232;
  --green-text:#7cbc2a;
  --ink:#222;
  --muted:#666;
  --panel:#efefef;
  --footer:#f8f8f8;
  --line:#cfcfcf;
}
*{margin:0;padding:0;box-sizing:border-box}
html,body{width:1200px;height:1200px;overflow:hidden}
body{position:relative;font-family:Arial,Helvetica,sans-serif;color:var(--ink);
  background:linear-gradient(#fff 0,#fff 300px,#e6efd9 440px,#efefef 440px,#efefef 1200px)}
.abs{position:absolute}
.brand{left:153px;top:36px;display:flex;align-items:center;gap:10px}
.brand-mark{width:22px;height:22px;background:var(--navy);border-radius:50%}
.brand-name{font-family:"Open Sans",sans-serif;font-weight:700;font-size:24px;color:var(--navy);letter-spacing:1px}
.account{right:141px;top:18px;font-family:"Open Sans",sans-serif;font-size:13px;color:#555;display:flex;align-items:center;gap:10px}
.account .sep{color:#999}
.phone{right:118px;top:66px;display:flex;align-items:center;gap:16px;font-weight:700;font-size:14px;color:#111}
.nav{left:130px;top:100px;width:940px;height:40px;background:linear-gradient(#1a30c6,var(--navy-deep));border-bottom:2px solid var(--green);box-shadow:0 2px 4px rgba(0,0,0,.3)}
.nav ul{list-style:none;display:flex;height:38px;align-items:center;padding-left:13px}
.nav li{font-family:"Open Sans",sans-serif;font-weight:600;font-size:13px;color:#fff;padding:0 16px;border-right:1px solid #2840c0;line-height:20px;position:relative}
.nav li:last-child{border-right:0}
.nav li.current::after{content:"";position:absolute;left:50%;bottom:-11px;margin-left:-5px;border:5px solid transparent;border-bottom-color:var(--green)}
.search{position:absolute;right:8px;top:9px;width:160px;height:20px;background:#fff;border:1px solid #999}
.search svg{position:absolute;right:3px;top:3px}
.hero{left:130px;top:140px;width:940px;height:300px;background:linear-gradient(100deg,#2b3a44 0%,#8fb3cc 30%,#cfe0ea 50%,#7fa3bd 62%,#0f1a20 78%,#06090c 100%)}
.caption{left:130px;top:200px;width:380px;height:120px;background:rgba(0,0,0,.72);color:#fff;padding:14px 30px}
.caption h1{font-family:"Open Sans",sans-serif;font-weight:400;font-size:27px;margin-bottom:12px}
.caption p{font-family:"Open Sans",sans-serif;font-size:12px;line-height:19px}
.main{left:130px;top:440px;width:940px;height:460px;background:#fff}
.welcome{left:155px;top:466px;font-family:"Noto Serif",serif;font-size:15px;color:var(--navy-deep);font-weight:700}
.welcome em{font-style:italic}
.intro{left:155px;top:492px;width:600px;font-size:12px;line-height:14.5px;color:#222}
.intro p{margin-bottom:9px}
.col-h{font-size:14px;font-weight:700;color:var(--green-text)}
.why{left:155px;top:627px;width:218px}
.why p{font-size:12px;line-height:14.5px;margin-top:7px}
.why p.indent{text-indent:36px}
.news{left:395px;top:627px;width:340px}
.news h3{margin-bottom:7px}
.news ul{list-style:none;margin-bottom:9px}
.news li{font-size:12px;line-height:14.5px;padding-left:17px;position:relative}
.news li::before{content:"";position:absolute;left:1px;top:5px;width:6px;height:6px;border-radius:50%;background:#222}
.qc-head{left:790px;top:402px;width:280px;height:38px;background:var(--green);color:#fff;font-weight:700;font-size:13px;display:flex;align-items:center;padding-left:20px;gap:12px}
.qc{left:790px;top:440px;width:280px;height:380px;background:var(--panel)}
.field{position:absolute;left:19px;font-size:12px;font-weight:700;color:#777}
.field span{display:inline-block;width:102px}
.field i{display:inline-block;width:140px;height:22px;background:#fff;border:1px solid #ccc;vertical-align:middle}
.comment-box{position:absolute;left:19px;top:204px;width:241px;height:120px;background:#fff;border:1px solid #ccc}
.submit{position:absolute;left:180px;top:337px;width:80px;height:30px;background:var(--green);color:#fff;font-weight:700;font-size:12px;display:flex;align-items:center;justify-content:center}
.footer{left:130px;top:900px;width:940px;height:160px;background:var(--footer);border-top:3px solid var(--line);box-shadow:0 2px 3px rgba(0,0,0,.15);font-family:"Open Sans",sans-serif;font-size:11px;color:#333}
.footer .col{position:absolute;top:18px;line-height:23px}
.footer .big{font-size:12.5px}
.social{position:absolute;left:260px;top:22px;display:flex;gap:13px}
.social span{width:26px;height:26px;border-radius:50%;background:#6b6b6b;display:block}
</style>
</head>
<body>
<div class="abs brand"><span class="brand-mark"></span><span class="brand-name">Torvik Capital</span></div>

<div class="abs account">
  <svg width="24" height="12" viewBox="0 0 24 12"><circle cx="5" cy="6" r="4" fill="none" stroke="#666" stroke-width="2"/><path d="M9 6h14M18 6v4M21 6v3" stroke="#666" stroke-width="2" fill="none"/></svg>
  <span>Account Login</span><span class="sep">|</span><span>Open Your Account</span>
</div>
<div class="abs phone">
  <span>Phone: 312.555.0148</span>
  <svg width="22" height="22" viewBox="0 0 24 24"><path d="M16 3c2 0 5 2 5 5l-3 1-2-3zM5 17c2 2 5 4 8 3l-1-3-3 0c-1-1-2-2-2-4l2-1-1-3-3 1c-1 2 0 5 0 7z" fill="#222"/></svg>
</div>

<nav class="abs nav">
  <ul>
    <li class="current">Home</li><li>About Us</li><li>Our Philosophy</li><li>Our Services</li><li>Investment Strategy</li><li>Compliance</li><li>Contact Us</li>
  </ul>
  <div class="search"><svg width="13" height="13" viewBox="0 0 14 14"><circle cx="5.5" cy="5.5" r="4" fill="none" stroke="#0b1a9c" stroke-width="2"/><path d="M8.5 8.5l4 4" stroke="#0b1a9c" stroke-width="2.5"/></svg></div>
</nav>

<div class="abs hero" role="img" aria-label="Photo looking up at glass office towers against a cloudy blue sky"></div>
<div class="abs caption">
  <h1>Portfolio management</h1>
  <p>Lorem ipsum dolor sit amet, consectetur adipiscing elit.<br>Donec varius pretium hendrerit. Cras ut sollicitudin erat.</p>
</div>

<div class="abs main"></div>
<h2 class="abs welcome"><em>Welcome to</em> TORVIK CAPITAL</h2>
<div class="abs intro">
  <p>Lorem ipsum dolor sit amet, consectetur adipiscing elit. Donec varius pretium hendrerit. Cras ut sollicitudin erat. Maecenas consectetur pellentesque quam, ut laoreet mauris varius ut. Maecenas ac vestibulum lacus. Mauris fermentum enim eu libero venenatis malesuada.</p>
  <p>Maecenas sollicitudin justo diam, nec vulputate lorem. In placerat dignissim ligula, nec condimentum velit placerat molestie. Cras et commodo risus. Nam varius, eros scelerisque pharetra molestie, metus nibh pretium urna, vel feugiat sem libero id tellus. Cum sociis natoque penatibus et magnis dis parturient montes, nascetur ridiculus mus. In mollis vestibulum orci in placerat</p>
</div>

<div class="abs why">
  <h3 class="col-h">Why Choose Torvik Capital?</h3>
  <p class="indent">Lorem ipsum dolor sit amet, consectetur adipiscing elit. Ut augue risus, pharetra in tincidunt non, mattis ut sapien. Pellentesque eu risus justo, sed porta magna.</p>
  <p>Nam lectus mauris, cursus nec tempus sit amet, tempus sed ipsum. Integer nibh dolor, suscipit eget porta a, dictum sed velit.</p>
</div>

<div class="abs news">
  <h3 class="col-h">Title of news headline one.</h3>
  <ul><li>Lorem ipsum dolor sit amet, consectetur adipiscing elit. Ut augue risus, pharetra in tincidunt non, mattis ut sapien.</li></ul>
  <h3 class="col-h">Title of news headline two.</h3>
  <ul><li>Lorem ipsum dolor sit amet, consectetur adipiscing elit. Ut augue risus, pharetra in tincidunt non, mattis ut sapien.</li></ul>
  <h3 class="col-h">Title of news headline three.</h3>
  <ul><li>Lorem ipsum dolor sit amet, consectetur adipiscing elit. Ut augue risus, pharetra in tincidunt non, mattis ut sapien.</li></ul>
</div>

<div class="abs qc-head">
  <svg width="18" height="14" viewBox="0 0 18 14"><path d="M1 7l8-6 8 6v6H1z M1 7l8 4 8-4" fill="none" stroke="#fff" stroke-width="1.3"/></svg>
  QUICK CONTACT
</div>
<form class="abs qc">
  <div class="field" style="top:24px"><span>First Name</span><i></i></div>
  <div class="field" style="top:61px"><span>Last Name</span><i></i></div>
  <div class="field" style="top:98px"><span>E-Mail</span><i></i></div>
  <div class="field" style="top:136px"><span>Phone Number</span><i></i></div>
  <div class="field" style="top:177px"><span>Comment*</span></div>
  <div class="comment-box"></div>
  <div class="submit">Submit</div>
</form>

<footer class="abs footer">
  <div class="col" style="left:19px">PO Box 40217<br>5550-1029384<br>Chicago, Illinois, USA<br>Tel: 15550172<br><span class="big">Email: hello@torvikcapital.com</span></div>
  <div class="social" aria-label="Social links"><span></span><span></span><span></span><span></span></div>
  <div class="col" style="left:500px">Terms of Use<br>Legal notice<br>Sitemap<br>Disclaimer</div>
  <div class="col" style="left:720px">Copyright © 2013<br>Torvik Capital Inc,<br>All rights reserved.</div>
</footer>
</body>
</html>
```